Flyer "Pinch Analysis"-Energy Optimization procedure for Industry

We need a flyer (1xA4 recto/verso )design for a new part of our business.

In Summary: we want to communicate that we are providing "Pinch Analysis" for the industry. It's an energy optimization procedure. We are a cutting edge engineering consulting group.

All details about project in the attached files

Target Market(s)

Engineering

Industry/Entity Type

Business

Font styles to use
Serif

Requirements
Must have
• Finale document in .ai format ready for printing
• More informations in attached files
Nice to have
• See attached files

```html
<!DOCTYPE html>
<html lang="fr">
<head>
<meta charset="utf-8">
<title>Analyse Pinch – Kelvin Step Engineering</title>
<link href="https://fonts.googleapis.com/css2?family=Syncopate:wght@700&family=Montserrat:wght@400;600;800&display=swap" rel="stylesheet">
<style>
  :root {
    --sky: #4cb8e8;
    --sky-deep: #1f6f99;
    --navy: #0d3358;
    --white: #ffffff;
    --panel: rgba(236, 246, 250, 0.9);
    --grid: #1a2e44;
  }
  html, body { margin: 0; padding: 0; overflow: hidden; }
  body { width: 849px; height: 1200px; background: var(--sky); }
  .flyer { position: relative; width: 849px; height: 1200px; overflow: hidden; background: var(--sky); }
  .plant-photo {
    position: absolute; left: 0; top: 330px; width: 849px; height: 854px;
    background: linear-gradient(180deg, #6cc3e8 0%, #4a9ec6 35%, #2d6f94 70%, #1d4f6e 100%);
  }
  .brand {
    position: absolute; left: 392px; top: 100px; display: flex; align-items: center; gap: 14px;
    color: var(--white); font-family: "Montserrat", sans-serif; font-weight: 600;
  }
  .brand-mark { width: 18px; height: 18px; background: var(--white); }
  .brand-name { font-size: 22px; letter-spacing: 2px; line-height: 1.15; text-transform: uppercase; }
  .rule { position: absolute; left: 0; top: 195px; width: 849px; height: 10px; background: var(--navy); }
  .headline {
    position: absolute; left: 40px; top: 232px; margin: 0;
    font-family: "Syncopate", sans-serif; font-weight: 700; font-size: 45px;
    color: var(--navy); letter-spacing: 1px; white-space: nowrap;
  }
  .tagline {
    position: absolute; left: 41px; margin: 0; color: var(--white);
    font-family: "Montserrat", sans-serif; font-weight: 400; font-size: 33px;
    letter-spacing: 2px; line-height: 49px; text-transform: uppercase;
  }
  .tagline-1 { top: 337px; }
  .tagline-2 { top: 411px; }
  .overlay { position: absolute; left: 0; top: 0; }
  .chart-title { font: 800 9.5px "Montserrat", sans-serif; fill: var(--navy); }
  .axis-tick { font: 600 7px "Montserrat", sans-serif; fill: var(--navy); }
  .axis-label { font: 800 8px "Montserrat", sans-serif; fill: var(--navy); }
  .footer-band { position: absolute; left: 0; bottom: 0; width: 849px; height: 16px; background: var(--sky); }
</style>
</head>
<body>
<div class="flyer">
  <div class="plant-photo" role="img" aria-label="Photo of an industrial boiler room with insulated tanks, pipes and valves, tinted blue"></div>

  <div class="brand">
    <span class="brand-mark"></span>
    <span class="brand-name">Kelvin Step<br>Engineering</span>
  </div>
  <div class="rule"></div>

  <h1 class="headline">ANALYSE PINCH -</h1>

  <svg class="overlay" width="849" height="1200" viewBox="0 0 849 1200">
    <!-- frame boxes -->
    <path d="M0 325 H452 a10 10 0 0 1 10 10 V388" fill="rgba(90,190,235,0.55)" stroke="#fff" stroke-width="3"/>
    <rect x="-4" y="325" width="466" height="64" fill="rgba(90,190,235,0.55)"/>
    <path d="M0 325 H452 a10 10 0 0 1 10 10 V392" fill="none" stroke="#fff" stroke-width="3"/>
    <path d="M0 392 H485 a10 10 0 0 1 10 10 V470 M0 528 H440" fill="none" stroke="#fff" stroke-width="3"/>
    <rect x="-4" y="392" width="499" height="136" fill="rgba(90,190,235,0.5)"/>
    <rect x="454" y="427" width="15" height="5" rx="2" fill="#fff"/>
    <!-- pipe lines -->
    <path d="M0 552 H432" fill="none" stroke="#fff" stroke-width="3"/>
    <path d="M802 520 H815 V1095 a10 10 0 0 0 10 10 H849" fill="none" stroke="#fff" stroke-width="3"/>
    <rect x="807" y="514" width="5" height="14" rx="2" fill="#fff"/>
    <path d="M742 722 V848 a10 10 0 0 0 10 10 H849" fill="none" stroke="#fff" stroke-width="3"/>
    <path d="M722 722 V700" fill="none" stroke="#fff" stroke-width="3"/>
    <rect x="712" y="742" width="20" height="5" rx="2" fill="#fff"/>
    <rect x="760" y="742" width="20" height="5" rx="2" fill="#fff"/>
    <path d="M722 722 V1000 M770 712 V1090" fill="none" stroke="#fff" stroke-width="3" opacity="0.9"/>

    <!-- chart panel -->
    <rect x="441" y="465" width="361" height="257" rx="12" fill="var(--panel)" stroke="#fff" stroke-width="3"/>
    <text class="chart-title" x="474" y="492">HOT AND COLD COMPOSITE CURVES</text>
    <g stroke="var(--grid)" stroke-width="0.8">
      <path d="M490 503 H781 M490 524 H781 M490 545 H781 M490 566 H781 M490 587 H781 M490 608 H781 M490 629 H781 M490 650 H781 M490 671 H781"/>
      <path d="M490 503 V671 M526.4 503 V671 M562.8 503 V671 M599.1 503 V671 M635.5 503 V671 M671.9 503 V671 M708.3 503 V671 M744.6 503 V671 M781 503 V671"/>
    </g>
    <g class="axis-tick" text-anchor="end">
      <text x="486" y="506">160</text><text x="486" y="527">140</text><text x="486" y="548">120</text>
      <text x="486" y="569">100</text><text x="486" y="590">80</text><text x="486" y="611">60</text>
      <text x="486" y="632">40</text><text x="486" y="653">20</text><text x="486" y="674">0</text>
    </g>
    <g class="axis-tick" text-anchor="middle">
      <text x="490" y="681">0</text><text x="526.4" y="681">100</text><text x="562.8" y="681">200</text>
      <text x="599.1" y="681">300</text><text x="635.5" y="681">400</text><text x="671.9" y="681">500</text>
      <text x="708.3" y="681">600</text><text x="744.6" y="681">700</text><text x="781" y="681">800</text>
    </g>
    <text class="axis-label" x="617" y="698" text-anchor="middle">HEAT FLOW (kW)</text>
    <text class="axis-label" transform="translate(467 587) rotate(-90)" text-anchor="middle">ACTUAL TEMPERATURE (°C)</text>
    <polyline points="490,652 526.4,645 544.6,637 580.9,618 584.6,613 586.4,597" fill="none" stroke="var(--navy)" stroke-width="3"/>
    <polyline points="515.5,658 628.2,608 646.4,526 752,526" fill="none" stroke="#4cb0e0" stroke-width="3"/>
  </svg>

  <p class="tagline tagline-1">En route vers</p>
  <p class="tagline tagline-2">La performance<br>énergétique</p>

  <div class="footer-band"></div>
</div>
</body>
</html>
```